Mezzanine Floor Manufacturer looking for a new business card design

We manufacture mezzanine floors and are providers of racking systems. We provide a range of items/services - simple rack repairs , full warehouse fit outs , manufacturer and install mezzanine floors , partitioning and large turnkey projects. Recently had a new website - www.corrowden-racking.co.uk and would like our business cards updating aswell . Our current card is single sided in the old logo colours (pdf attached) and needs updating.

Target Market(s)

We deal with large projects/ multi national companies and also smaller projects and companies throughout the UK ranging from a single warehouse to a large multi site company.

Industry/Entity Type

Business

Contact Information for Business Card

Will have job title,tel no's, email ,website address etc like example pdf

Requirements
Must have
• Hi - needs to use the colours of the logo & new website. Card needs to be professional

```html
<!DOCTYPE html>
<html lang="en">
<head>
<meta charset="utf-8">
<title>Corrowden Racking – Business Card</title>
<link rel="stylesheet" href="https://fonts.googleapis.com/css2?family=Arimo:wght@400;700&display=swap">
<style>
  :root {
    --red: #c8161e;
    --grey: #7d7877;
    --text-grey: #555;
    --white: #ffffff;
    --backdrop: #e9e7e4;
    --font: "Arimo", Arial, sans-serif;
  }
  * { box-sizing: border-box; margin: 0; padding: 0; }
  html, body { width: 1200px; height: 950px; overflow: hidden; }
  body { background: var(--backdrop); font-family: var(--font); position: relative; }

  .card {
    position: absolute; left: 260px; width: 680px; height: 400px;
    background: var(--white); overflow: hidden;
    box-shadow: 0 6px 18px rgba(0,0,0,.18);
  }
  .card--back { top: 50px; }
  .card--front { top: 500px; }

  .brand-mark { position: absolute; display: flex; align-items: center; gap: 10px; white-space: nowrap; }
  .brand-mark__dot { width: 30px; height: 30px; border-radius: 50%; background: var(--red); flex: none; }
  .brand-mark__name { color: var(--red); font-weight: 700; font-size: 32px; }

  /* back */
  .card--back .brand-mark { left: 50%; top: 150px; transform: translateX(-50%); }
  .card--back .website {
    position: absolute; left: 0; right: 0; top: 226px; text-align: center;
    color: var(--grey); font-size: 16px; letter-spacing: 3px;
  }
  .social { position: absolute; right: 26px; top: 78px; display: flex; gap: 5px; }
  .social span { width: 16px; height: 16px; border-radius: 50%; background: #222; }

  /* front */
  .swoosh { position: absolute; inset: 0; }
  .card--front .brand-mark { left: 40px; top: 62px; gap: 8px; }
  .card--front .brand-mark__dot { width: 20px; height: 20px; }
  .card--front .brand-mark__name { font-size: 17px; }
  .company { position: absolute; left: 40px; top: 94px; color: var(--red); font-weight: 700; font-size: 44px; white-space: nowrap; }
  .contacts { position: absolute; left: 40px; top: 158px; list-style: none; }
  .contacts li { display: flex; align-items: center; gap: 8px; color: var(--text-grey); font-size: 17px; line-height: 23px; white-space: nowrap; }
  .contacts svg { width: 16px; height: 16px; fill: var(--red); flex: none; }
  .person { position: absolute; right: 34px; top: 118px; text-align: right; color: var(--white); }
  .person__name { font-weight: 700; font-size: 22px; }
  .person__role { font-size: 18px; margin-top: 2px; }
  .address {
    position: absolute; right: 162px; top: 292px; text-align: right;
    color: var(--text-grey); font-size: 16px; line-height: 21px; font-style: normal; white-space: nowrap;
  }
</style>
</head>
<body>
  <section class="card card--back">
    <div class="social"><span></span><span></span><span></span><span></span></div>
    <div class="brand-mark"><span class="brand-mark__dot"></span><span class="brand-mark__name">Corrowden Racking</span></div>
    <p class="website">www.corrowden-racking.co.uk</p>
  </section>

  <section class="card card--front">
    <svg class="swoosh" viewBox="0 0 680 400" width="680" height="400" aria-hidden="true">
      <path d="M0 0 H680 V400 H600 C596 200 450 30 0 8 Z" fill="var(--red)"/>
      <path d="M0 14 C445 36 588 205 592 400 H568 C562 222 425 60 0 28 Z" fill="var(--grey)"/>
    </svg>

    <div class="brand-mark"><span class="brand-mark__dot"></span><span class="brand-mark__name">Corrowden Racking</span></div>
    <h1 class="company">Corrowden</h1>

    <ul class="contacts">
      <li><svg viewBox="0 0 16 16"><path d="M3 2h3l1 4-2 1c1 2 2 3 4 4l1-2 4 1v3c0 1-1 2-2 2C6 15 1 10 1 4c0-1 1-2 2-2z"/></svg>01632 960418</li>
      <li><svg viewBox="0 0 16 16"><path d="M4 1h8v14H4zM6 3v9h4V3z"/></svg>07700 900312</li>
      <li><svg viewBox="0 0 16 16"><path d="M4 1h7v5H4zM1 6h14v8H1zm3 3v3h8V9z"/></svg>01632 960419</li>
      <li><svg viewBox="0 0 16 16"><path d="M1 3h14v10H1zM2 4l6 5 6-5z"/></svg>daniel@corrowden-racking.co.uk</li>
    </ul>

    <div class="person">
      <p class="person__name">Daniel Hartley</p>
      <p class="person__role">Technical sales</p>
    </div>

    <address class="address">
      Millstone Way<br>
      Ashcombe Trade Park<br>
      Hollinsford, Derbyshire DE9 4QX<br>
      www.corrowden-racking.co.uk
    </address>
  </section>
</body>
</html>
```